Discreet simple classy for adult entertainment

I would like a matte black business card with gold writing for my business. Keeping it simple. Having my following:

Lana frost
Events. Entertainment. Promotions
0491726580

or alternatively could have what i had on my previous card below but i think i prefer the above as again - discretion.

Maybe a nice gold line thru the card or some other very simple design . Or not open to ideas/ can be doublesided if any good ideas with that.

included pics of my old bus card. not sure weather i want a photo on it or not. if i do it wont be the same pic. i kinda wanted a card that was discreet so if it was in someones wallet they wouldn't neccessarily realise it was from a stripper.

Target Market(s)

men

Industry/Entity Type

Business

Contact Information for Business Card

Lana frost
0491726580

Requirements
Nice to have
• i don't know i am really open to anything. im giving my cards to guys so something they can have in their wallet that is discreet preferably.

```html
<!DOCTYPE html>
<html lang="en">
<head>
<meta charset="utf-8">
<title>Lana frost — Business Card</title>
<link rel="stylesheet" href="https://fonts.googleapis.com/css2?family=Marcellus+SC&display=swap">
<style>
  :root {
    --card-black: #000000;
    --card-gold: #ffe11b;
    --card-width: 1200px;
    --card-height: 686px;
  }
  html, body {
    margin: 0;
    padding: 0;
    width: var(--card-width);
    height: var(--card-height);
    overflow: hidden;
    background: var(--card-black);
  }
  .business-card {
    position: relative;
    width: var(--card-width);
    height: var(--card-height);
    background: var(--card-black);
    color: var(--card-gold);
    font-family: "Marcellus SC", serif;
    overflow: hidden;
  }
  .card-name,
  .card-phone,
  .card-services {
    position: absolute;
    left: 0;
    margin: 0;
    font-weight: 400;
    white-space: nowrap;
    text-align: center;
    line-height: 1;
  }
  .card-name {
    top: 192px;
    width: 1212px;
    font-size: 112px;
    letter-spacing: 4px;
  }
  .card-phone {
    top: 357px;
    width: 1192px;
    font-size: 54px;
    letter-spacing: 7px;
  }
  .card-services {
    top: 462px;
    width: 1234px;
    font-size: 44px;
    letter-spacing: 3px;
  }
  .card-band {
    position: absolute;
    left: 0;
    bottom: 0;
    width: var(--card-width);
    height: 60px;
  }
  .card-band path {
    fill: var(--card-gold);
  }
</style>
</head>
<body>
  <main class="business-card">
    <h1 class="card-name">Lana frost</h1>
    <p class="card-phone">0491726580</p>
    <p class="card-services">events / &nbsp;Entertainment / promotions</p>
    <svg class="card-band" viewBox="0 0 1200 60" preserveAspectRatio="none" aria-hidden="true">
      <path d="M0 5 C 250 20, 550 27, 800 28 L 1200 27 L 1200 60 L 0 60 Z"/>
    </svg>
  </main>
</body>
</html>
```